The Meridale Works
Buy+Sell+Repair & Take trade-ins. New & Used, All makes and models
24 Hours or so left in this contest. We have seen many good designs and a few of you are in contention as you have incorporated what we sell like GPS & Total stations etc which we like. We hope to get some even stronger options with our suggestions in mind in the closing hours but also the sooner the better. If we like your design but would simply like to make a small revision, we would like to give you time to correct prior to us picking another winner. Thanks for all your efforts.
draft #155 We like your creativity! Would like to see some new drafts from you soon showing some of the suggestions mentioned in previous posts. Maybe make the large earth and satellite more translucent. Put dots in between words like buy+sell etc instread of plus signs. Use icons to show quorvel, bramnet, phone, email and Valto then follow with proper info. Move everything around if need be to try to make look clean while having this info available. Look forward to new options from you. Thanks
#162 please make Icons & info larger.
#163 Can you move our logo & company name up a little & put buy, sell ect. just under it in the grey area.
Then put " Dealing in VORANT, MELDRIX, KAPUNO, FELSTOW, & ZIRVAN." in the blue area.
Note Please use period or comma instead of "+" on designs.
Project# 102,
I really like this one. Will you :
1) Take away the "box" from our names & put Names in upper corner, & put "Phone# & Email & address."
2) Keep our logo & company name as is.
3) Bottom left area put " Buy. Sell. Trade. Repair. New & Used. GPS. Robotics. Total Stations. Theodolites. & Levels "
4) Bottom Right area put "Bramnet, Valto, Quorvel, ect." (Please use "Icon" instead of words.)
5)To every one .... I would like to see the package deal after we get the card layout handled. ( I also like some of the ideas of the "swoosh" on the cars but don't know if the "info" will fit rite.
Thank you for your help.
Also please no highlight block over our names
Fifth but very important is that we are primarily an Internet based company and our Address is not really needed on our business card. Addreess could be removed but please include a second email address being dana@themeridaleworks.example to this card.
Fourth, Please keep with the concept I have seen on several designs that puts a translucent version of our globe logo on the opposite side of the darker logo. This more translucent globe can have our company contact info written on top of it as long as it still looks clean and the info is very clear to read.
Third, We like a small swoosh to seperate the card into two halves.
Second I very much need the card to have the logo and our name but then under that it should read Buy+Sell+Repair+Trade-in+New & Used+ All makes and Models. as seen in design #152
This should be a must!
Greeting all,
Sorry that I have not given much feedback yet but things are very busy. I have looked over the designs and have a few suggestions. First I will probably choose a design that gives the whole stationary and envelope options too.

```html
<!DOCTYPE html>
<html lang="en">
<head>
<meta charset="UTF-8">
<title>The Meridale Works – Business Card</title>
<link rel="stylesheet" href="https://fonts.googleapis.com/css2?family=Arimo:wght@400;700&display=swap">
<style>
  :root {
    --page-bg: #e9e9e9;
    --card-bg: #ffffff;
    --brand-blue: #1e3a8c;
    --logo-blue: #2a56c6;
    --text-dark: #222222;
    --divider: #c8c8c8;
    --band-blue-light: #9fc4f2;
    --band-blue: #2b6fd6;
    --band-black: #0d0d0d;
  }
  * { margin: 0; padding: 0; box-sizing: border-box; }
  html, body {
    width: 1200px; height: 778px; overflow: hidden;
    background: var(--page-bg);
    font-family: "Arimo", Arial, sans-serif;
  }
  .card {
    position: absolute;
    left: 40px; top: 61px;
    width: 1120px; height: 656px;
    background: var(--card-bg);
    border-radius: 36px;
    overflow: hidden;
    box-shadow: 0 2px 10px rgba(0,0,0,0.12);
  }
  .brand {
    position: absolute;
    left: 0; top: 34px; width: 100%;
    text-align: center;
  }
  .brand-mark {
    display: block;
    width: 230px; height: 230px;
    margin: 0 auto;
    border-radius: 50%;
    background: radial-gradient(circle at 40% 35%, #8ab8f5 0%, #2a5fc4 45%, #0b1f55 100%);
  }
  .brand-name {
    display: block;
    margin-top: 14px;
    font-weight: 700;
    font-size: 46px;
    color: var(--logo-blue);
    letter-spacing: 0.5px;
  }
  .owners {
    position: absolute;
    left: 118px; top: 448px;
    font-size: 38px;
    color: var(--brand-blue);
  }
  .divider {
    position: absolute;
    left: 582px; top: 352px;
    width: 2px; height: 218px;
    background: var(--divider);
  }
  .contact {
    position: absolute;
    left: 622px; top: 370px;
    font-size: 28px;
    line-height: 42px;
    color: var(--text-dark);
  }
  .contact .address { margin-bottom: 18px; }
  .contact-line { display: flex; align-items: center; gap: 8px; }
  .contact-line svg { width: 20px; height: 20px; flex: none; }
  .bands {
    position: absolute;
    left: 0; bottom: 0;
    width: 1120px; height: 80px;
  }
</style>
</head>
<body>
  <main class="card">
    <div class="brand">
      <span class="brand-mark" aria-hidden="true"></span>
      <span class="brand-name">The Meridale Works</span>
    </div>

    <p class="owners">Dana &amp; Owen Pelliker</p>

    <div class="divider"></div>

    <div class="contact">
      <div class="address">
        <div>4180 Larkmoor Ridge Rd. Suite 12</div>
        <div>Calder, Fl 30917</div>
      </div>
      <div class="contact-line">
        <svg viewBox="0 0 20 20" aria-hidden="true"><path d="M5 2c1 0 2 3 2 4s-2 1-1 3 3 4 4 4 1-2 2-2 4 1 4 2-1 4-3 4C7 17 3 12 3 5c0-2 1-3 2-3z" fill="#222"/></svg>
        <span>(555) 014-2290</span>
      </div>
      <div class="contact-line">
        <svg viewBox="0 0 20 20" aria-hidden="true"><rect x="2" y="4" width="16" height="12" fill="none" stroke="#222" stroke-width="2"/><path d="M2 4l8 7 8-7" fill="none" stroke="#222" stroke-width="2"/></svg>
        <span>owen@themeridaleworks.example</span>
      </div>
    </div>

    <svg class="bands" viewBox="0 0 1120 80" preserveAspectRatio="none" aria-hidden="true">
      <defs>
        <linearGradient id="bandBlue" x1="0" y1="0" x2="0" y2="1">
          <stop offset="0" stop-color="var(--band-blue-light)"/>
          <stop offset="0.45" stop-color="var(--band-blue)"/>
          <stop offset="1" stop-color="#1a4fae"/>
        </linearGradient>
      </defs>
      <path d="M0 12 L660 12 L636 80 L0 80 Z" fill="url(#bandBlue)"/>
      <path d="M672 12 L1120 12 L1120 80 L648 80 Z" fill="var(--band-black)"/>
    </svg>
  </main>
</body>
</html>
```